Business Card For Video Production Company

Please NOTE: I've added some info to the must haves that I should have included at the start. Thank you.

I need a business card design for my video production company based in Orlando called Halvard Lens Productions. Our work consists of web video marketing (web videos), training videos, sales videos, conference and seminar video production...basically a lot of corporate based work.

We work with successful small businesses, not-for-profits and some Summit 700 type groups. We bring a lot of knowledge, experience and attention to detail to every project.

I'd like something that communicates strength, confidence, integrity, as well as creative vision. I want to stay away from the standard icons of the media and film industry. I'd like to emphasize the colors of my logo, and also the colors of my website which has a white background. Simple is good.

Our budgets are moderate...generally $1500 to $5000.

www.halvardlens.tv

PS...We don't do weddings or recitals, or that type of production.
Updates

I want to thank all the designers for your updates. There's way too many to be able to give feedback on for all. I hope you understand that. But wow…there are so many great designs everyone has offered. I can't thank you enough…each and everyone. I hope to make my decision soon. I'm not accepting anymore designs from new designers. Dean-

Target Market(s)

Successful small businesses, marketing directors, corporate communication directors, training and human resources professionals. forward thinking not-for profits. Since my company is based in Central Florida, most of my work comes from this area too.

Industry/Entity Type

Marketing

Requirements
Must have
• website address, www.halvardlens.tv
phone number, 407-555-2937
email address, dean@halvardlens.tv

Title
Dean Halvard
Owner/Creative Director

I'd like to have a single line that goes across illustrating our services, maybe separated with bullet points:

Marketing Videos, Corporate Videos, Conference & Seminar Video Production
Should not have
• No film or video icons.
No need to pull language or copy from my website.

```html
<!DOCTYPE html>
<html lang="en">
<head>
<meta charset="utf-8">
<title>Halvard Lens Productions – Business Card</title>
<link rel="stylesheet" href="https://fonts.googleapis.com/css2?family=Arimo:wght@400;700&display=swap">
<style>
  :root {
    --page-bg: #ffffff;
    --card-bg: #ffffff;
    --card-border: #a9a9a9;
    --brand-blue: #0090d6;
    --brand-grey: #55575a;
    --text-dark: #333333;
  }
  * { margin: 0; padding: 0; box-sizing: border-box; }
  html, body {
    width: 1200px;
    height: 730px;
    overflow: hidden;
    background: var(--page-bg);
    font-family: "Arimo", Arial, sans-serif;
  }
  .canvas { position: relative; width: 1200px; height: 730px; }

  .card {
    position: absolute;
    top: 15px;
    width: 325px;
    height: 180px;
    background: var(--card-bg);
    border: 1px solid var(--card-border);
    overflow: hidden;
  }
  .card--front { left: 56px; }
  .card--back { left: 507px; }

  /* Front */
  .brand {
    position: absolute;
    left: 15px;
    top: 7px;
    display: flex;
    align-items: center;
    gap: 14px;
  }
  .brand__mark {
    width: 62px;
    height: 62px;
    background: var(--brand-blue);
  }
  .brand__name {
    color: var(--brand-grey);
    font-weight: 700;
    line-height: 1;
  }
  .brand__name-main { display: block; font-size: 24px; letter-spacing: 0.5px; }
  .brand__name-sub { display: block; font-size: 12px; letter-spacing: 0.3px; margin-top: 5px; }

  .person {
    position: absolute;
    left: 15px;
    top: 98px;
    font-size: 7.5px;
    line-height: 9.5px;
    color: var(--text-dark);
    word-spacing: 1px;
  }

  .contact {
    position: absolute;
    left: 15px;
    top: 141px;
    list-style: none;
    font-size: 7px;
    line-height: 9.2px;
    color: var(--text-dark);
  }
  .contact__label { color: var(--brand-blue); margin-right: 3px; }

  /* Back */
  .services__title {
    position: absolute;
    left: 17px;
    top: 57px;
    font-size: 9px;
    font-weight: 400;
    color: var(--brand-blue);
    word-spacing: 2px;
  }
  .services__list {
    position: absolute;
    left: 7px;
    top: 74px;
    list-style: none;
    font-size: 8.5px;
    line-height: 15.8px;
    color: var(--text-dark);
    word-spacing: 2px;
  }
  .services__list li::before {
    content: ".";
    display: inline-block;
    width: 8px;
    color: var(--text-dark);
  }
  .card__band {
    position: absolute;
    left: 0;
    right: 0;
    bottom: 0;
    height: 10px;
    background: var(--brand-blue);
  }
</style>
</head>
<body>
<main class="canvas">
  <section class="card card--front" aria-label="Business card front">
    <div class="brand">
      <div class="brand__mark"></div>
      <div class="brand__name">
        <span class="brand__name-main">Halvard Lens</span>
        <span class="brand__name-sub">PRODUCTIONS</span>
      </div>
    </div>

    <p class="person">Dean Halvard<br>Owner/Creative Director</p>

    <ul class="contact">
      <li><span class="contact__label">website:</span> www.halvardlens.tv</li>
      <li><span class="contact__label">phone:</span> 407-555-2937</li>
      <li><span class="contact__label">email:</span> dean@halvardlens.tv</li>
    </ul>
  </section>

  <section class="card card--back" aria-label="Business card back">
    <h2 class="services__title">Our Service</h2>
    <ul class="services__list">
      <li>Marketing Videos</li>
      <li>Corporate Videos</li>
      <li>Conference &amp; Seminar</li>
      <li>Video Production</li>
    </ul>
    <div class="card__band"></div>
  </section>
</main>
</body>
</html>
```